Inviting A6 Flyer for Church membership

We need an A6 size flyer for the church. We are looking for something fresh, inviting and impactful. Church new logo and current flyer design attached.
Back text as follows:
We would love to have you join us as our SPECIAL GUEST this Sunday at 10am.
You can find us at Harvest Gateway Family Church, 17-19 Meadowbrook Lane
(Behind Farley), Pellham Brook Village,KL7 2RT
For more information or for a chat, please call us on 07614 290457 / 07781 504316 or email church@hgfcuk.org
Target Market(s)
Church
Industry/Entity Type
Church
Colors
Designer to choose colors to be used in the design.
Requirements
Must have
- fresh, inviting and impactful.
- Chruch logo (attached)
Should not have
- Too much going on

```html
<!DOCTYPE html>
<html lang="en">
<head>
<meta charset="utf-8">
<title>Harvest Gateway Ministries – Invitation Flyer</title>
<link href="https://fonts.googleapis.com/css2?family=Cinzel:wght@400;700&family=Arvo:wght@400;700&family=Open+Sans:wght@400&display=swap" rel="stylesheet">
<style>
  :root{
    --backdrop:#c39a6e;
    --white:#ffffff;
    --brand-red:#a3331f;
    --brand-blue:#1665a8;
    --deep-blue:#0b4f96;
    --light-blue:#1b8fd0;
    --steel:#9fb4c0;
    --slate:#4d6673;
    --cream:#f3e8d6;
    --ink:#1d1d1d;
  }
  *{margin:0;padding:0;box-sizing:border-box}
  html,body{width:878px;height:1200px;overflow:hidden;background:var(--backdrop)}
  .card{position:absolute;left:74px;width:739px;height:524px;overflow:hidden}
  .card svg.bg{position:absolute;inset:0}
  .front{top:66px;background:var(--white)}
  .back{top:619px;background:var(--brand-red)}

  .front .mark{position:absolute;left:278px;top:50px;width:200px;height:200px;border-radius:50%;
    background:radial-gradient(circle at 40% 35%,var(--light-blue),var(--deep-blue));}
  .front .name{position:absolute;left:0;width:739px;text-align:center;font-family:"Cinzel",serif;
    font-weight:700;color:var(--brand-red);line-height:1}
  .front .name-top{top:265px;font-size:44px}
  .front .name-sub{top:313px;font-size:40px}
  .front .rule{position:absolute;left:90px;top:351px;width:551px;height:1px;background:var(--slate)}
  .front .tagline{position:absolute;left:0;top:358px;width:739px;text-align:center;font-family:"Cinzel",serif;
    font-size:18px;line-height:24px;color:var(--slate)}

  .email{position:absolute;display:flex;align-items:center;gap:8px;color:var(--white);
    font-family:"Cinzel",serif;font-family:"Open Sans",sans-serif}
  .front .email{left:482px;top:474px;font-size:20px}
  .back .email{left:485px;top:476px;font-size:24px}

  .back .dot{position:absolute;border-radius:50%;
    background:radial-gradient(circle at 40% 35%,var(--light-blue),var(--deep-blue));
    box-shadow:0 0 0 3px var(--steel)}
  .back .dot-left{left:30px;top:29px;width:128px;height:128px}
  .back .dot-right{left:607px;top:373px;width:96px;height:96px}
  .back .flowers{position:absolute;left:598px;top:56px;width:141px;height:320px;
    background:linear-gradient(180deg,#eab3b4 0%,#e9a9ad 40%,#c9b5a0 75%,#b9a58e 100%);
    -webkit-mask-image:linear-gradient(90deg,transparent 0%,#000 35%);
    mask-image:linear-gradient(90deg,transparent 0%,#000 35%)}
  .back .copy{position:absolute;left:110px;width:520px;text-align:center;font-family:"Arvo",serif;color:var(--ink)}
  .invite{top:108px;font-size:19px;font-weight:700;line-height:26px}
  .invite .hl{color:var(--brand-blue)}
  .findus{top:181px;font-size:20px;color:var(--brand-red)}
  .venue{top:213px;font-size:28px;color:var(--brand-blue);left:60px!important;width:620px!important}
  .address{top:252px;font-size:19px;font-weight:700;line-height:28px}
  .info{top:344px;font-size:17px;font-weight:700}
  .phones{top:376px;font-size:24px;font-weight:700;color:var(--brand-red)}
  .oremail{top:418px;font-size:18px;font-family:"Open Sans",sans-serif!important}
</style>
</head>
<body>

<section class="card front">
  <svg class="bg" width="739" height="524" viewBox="0 0 739 524">
    <defs>
      <linearGradient id="frontBlue" x1="0" x2="1">
        <stop offset="0" stop-color="#1b8fd0"/><stop offset="1" stop-color="#0b4f96"/>
      </linearGradient>
    </defs>
    <path d="M0,462 Q340,540 739,352 L739,524 L0,524 Z" fill="#9fb4c0"/>
    <path d="M0,476 Q350,545 739,378 L739,524 L0,524 Z" fill="url(#frontBlue)"/>
  </svg>
  <div class="mark" aria-hidden="true"></div>
  <div class="name name-top">HARVEST GATEWAY</div>
  <div class="name name-sub">MINISTRIES</div>
  <div class="rule"></div>
  <p class="tagline">WORSHIPPING GOD, PREACHING THE WORD<br>AND DOING THE WORKS OF JESUS CHRIST.</p>
  <div class="email">
    <svg width="22" height="18" viewBox="0 0 22 18"><rect x="1" y="3" width="20" height="14" fill="#fff" stroke="#9fb4c0"/><path d="M1,3 L11,11 L21,3" fill="none" stroke="#9fb4c0"/></svg>
    church@hgfcuk.org
  </div>
</section>

<section class="card back">
  <svg class="bg" width="739" height="524" viewBox="0 0 739 524">
    <path d="M0,172 Q330,20 739,62 L739,88 Q330,50 0,216 Z" fill="#1665a8"/>
    <path d="M0,216 Q330,50 739,88 L739,354 Q420,500 0,462 Z" fill="#f3e8d6"/>
    <path d="M0,462 Q420,500 739,354 L739,368 Q420,515 0,474 Z" fill="#1665a8"/>
  </svg>
  <div class="flowers" role="img" aria-label="Photo of pink roses in a stone pot"></div>
  <div class="dot dot-left" aria-hidden="true"></div>
  <div class="dot dot-right" aria-hidden="true"></div>

  <p class="copy invite">We would love to have youjoin us as<br>our <span class="hl">SPECIAL GUEST</span> this <span class="hl">SUNDAY AT 10AM</span></p>
  <p class="copy findus">You can find us at</p>
  <p class="copy venue">Harvest Gateway Family Church,</p>
  <p class="copy address">17-19 Meadowbrook Lane (Behind Farley),<br>Pellham Brook Village, KL7 2RT</p>
  <p class="copy info">For more information or for a chat,please call us on</p>
  <p class="copy phones">07614 290457 / 07781 504316</p>
  <p class="copy oremail">or email.</p>
  <div class="email">
    <svg width="28" height="22" viewBox="0 0 22 18"><rect x="1" y="3" width="20" height="14" fill="#fff" stroke="#9fb4c0"/><path d="M1,3 L11,11 L21,3" fill="none" stroke="#9fb4c0"/></svg>
    church@hgfcuk.org
  </div>
</section>

</body>
</html>
```